I need a website designed. I am a mortgage loan officer and would like to have a website for me and my team where i can post resources, videos and blog information for my clients. A website like themorrowcrew.net .

The theme is - The Halvick Crew - Home Loan Group powered by Bramfield Home Loans -

Target Market(s)

B2B (Real Estate Agents)and B2C (Home buyers and refinancing)

Industry/Entity Type

Mortgage Lender

Coding

Coded - Design and coding required

Number of Pages Required

5+ page

Font styles to use
Serif
Sans Serif

Colors

Designer to choose colors to be used in the design.

Requirements
Must have
• Disclaimers: Licensed by the Office of Trade Stewardship under the Regional Credit Providers Act. Loans made or arranged pursuant to a Regional Credit Providers Act License. Equal Housing Lender Bramfield Cannot Accept mortgage applications for properties located in New York via this site
• Mobile Friendly
Nice to have
• Main Links: Home, About Us(see team flyer), Mortgage 101, Contact Us (formly form)

```html
<!DOCTYPE html>
<html lang="en">
<head>
<meta charset="utf-8">
<title>The Halvick Crew – Home Loan Group</title>
<link href="https://fonts.googleapis.com/css2?family=Oswald:wght@400;500;600&family=Hind:wght@400;500;600&display=swap" rel="stylesheet">
<style>
:root{
  --blue:#1a6fb9;
  --blue-dark:#155b99;
  --navy:#0f1d2e;
  --ink:#222;
  --text:#444;
  --muted:#777;
  --grey:#eeeeee;
  --white:#fff;
}
*{box-sizing:border-box;margin:0;padding:0}
html,body{width:1200px;height:3782px;overflow:hidden}
body{font-family:"Hind",sans-serif;color:var(--text);background:var(--white);position:relative}
section,header,footer{position:absolute;left:0;width:1200px}
.center{text-align:center}
.btn{display:inline-block;background:var(--blue);color:var(--white);font-family:"Hind",sans-serif;font-weight:600;font-size:15px;letter-spacing:.5px;border-radius:20px;padding:9px 26px 7px;text-transform:uppercase;line-height:1.2}
.section-title{font-family:"Oswald",sans-serif;font-size:34px;font-weight:500;color:var(--ink);text-transform:uppercase;text-align:center;letter-spacing:.5px}
.section-title span{color:var(--blue)}
.rule{width:48px;height:3px;background:var(--blue);margin:10px auto 0}

/* header */
.site-header{top:0;height:121px;background:var(--white)}
.brand{position:absolute;left:76px;top:14px;display:flex;align-items:center;gap:12px}
.brand-mark{width:46px;height:46px;background:var(--blue)}
.brand-name{font-family:"Oswald",sans-serif;font-size:30px;font-weight:500;color:var(--blue);line-height:1}
.brand-sub{font-family:"Oswald",sans-serif;font-size:13px;color:var(--blue);letter-spacing:3px;border-top:1px solid var(--blue);margin-top:4px;padding-top:2px}
.head-contact{position:absolute;top:8px;display:flex;align-items:center;gap:14px;font-size:17px;color:var(--ink);line-height:1.2}
.icon-circle{width:54px;height:54px;border-radius:50%;background:var(--blue);display:flex;align-items:center;justify-content:center}
.phone-big{font-family:"Oswald",sans-serif;font-size:30px;font-weight:500;color:var(--blue);line-height:1}
.main-nav{position:absolute;right:80px;top:86px;display:flex;gap:34px;font-family:"Oswald",sans-serif;font-size:16px;font-weight:500;color:var(--ink)}
.main-nav .active{color:var(--blue)}

/* hero */
.hero{top:121px;height:542px;background:radial-gradient(circle at 25% 30%,#4a6a8a 0,#1e3147 40%,#0d1522 80%)}
.hero-photo{position:absolute;inset:0;background:linear-gradient(90deg,rgba(20,35,55,.2),rgba(40,50,60,.1) 60%,rgba(150,120,90,.45) 85%,rgba(20,25,35,.2))}
.hero-copy{position:absolute;left:0;right:0;top:140px;text-align:center;color:var(--white)}
.hero-copy h1{font-family:"Oswald",sans-serif;font-size:44px;font-weight:500;letter-spacing:1px}
.hero-copy p{font-size:19px;line-height:1.35;width:640px;margin:8px auto 18px}
.hero-copy .btn{font-size:20px;padding:13px 32px 11px;border-radius:28px}
.hero-arrows{position:absolute;top:470px;left:560px;display:flex;gap:40px}

/* intro */
.intro{top:663px;height:615px;background:var(--grey)}
.intro-head{position:absolute;left:0;right:0;top:54px}
.lead{position:absolute;left:90px;top:120px;width:1020px;text-align:center;font-size:14px;line-height:1.6;color:var(--text)}
.intro-btn{position:absolute;left:0;right:0;top:210px;text-align:center}
.cards{position:absolute;left:76px;display:flex;gap:32px}
.card{width:330px}
.card-media{height:210px;position:relative}
.card-text{font-size:14.5px;line-height:1.5;text-align:center;margin-top:16px;padding:0 8px}
.play{position:absolute;left:50%;top:50%;width:64px;height:64px;margin:-32px 0 0 -32px;border:3px solid var(--white);border-radius:50%}
.play::after{content:"";position:absolute;left:24px;top:17px;border-left:20px solid var(--white);border-top:12px solid transparent;border-bottom:12px solid transparent}

/* blog */
.blog{top:1278px;height:507px;background:var(--white)}
.blog .section-title{margin-top:48px}
.date-badge{position:absolute;left:50%;top:50%;transform:translate(-50%,-50%);width:62px;height:76px;background:rgba(30,30,30,.8);color:var(--white);text-align:center;font-family:"Oswald",sans-serif;padding-top:8px}
.date-badge b{display:block;font-size:26px;font-weight:500;line-height:1}
.date-badge small{font-size:14px;border-top:1px solid #fff;display:block;margin:4px 10px 0;padding-top:3px}

/* team */
.team{top:1785px;height:1001px;background:var(--grey)}
.team .section-title{margin-top:48px}
.lead-photo{position:absolute;left:282px;top:105px;width:278px;height:278px;border-radius:50%;border:6px solid var(--blue);background:radial-gradient(circle at 50% 40%,#c9a58a,#8a6a55 60%,#dfe3e8 61%)}
.lead-info{position:absolute;left:608px;top:180px;color:var(--ink);font-size:16px;line-height:1.4}
.lead-info h3{font-family:"Oswald",sans-serif;font-size:30px;font-weight:400;color:var(--blue);line-height:1}
.lead-info .role{color:var(--blue);font-size:16px;margin:8px 0 14px}
.bio{position:absolute;left:176px;top:400px;width:850px;text-align:center;font-size:16px;line-height:1.55;color:var(--ink)}
.member{position:absolute;top:578px;width:320px;text-align:center;color:var(--ink);font-size:14px;line-height:1.5}
.member .avatar{width:192px;height:192px;border-radius:50%;margin:0 auto 22px;background:radial-gradient(circle at 50% 42%,#b98f73,#6b5245 55%,#d9dde2 56%)}
.member h4{font-family:"Oswald",sans-serif;font-size:19px;font-weight:500;color:var(--blue);margin-bottom:6px}
.socials{display:flex;justify-content:center;gap:10px;margin-top:8px}
.socials i{width:12px;height:12px;border-radius:50%;background:var(--ink);display:block}

/* resources */
.resources{top:2786px;height:353px;background:linear-gradient(180deg,#b9c7d2,#d6dde2 45%,#c7d0d4)}
.resources-veil{position:absolute;inset:0;background:rgba(255,255,255,.55)}
.resources-inner{position:relative;text-align:center}
.resources .section-title{padding-top:44px;font-size:30px}
.resources p{width:1040px;margin:30px auto 20px;font-size:15.5px;line-height:1.55;color:var(--ink)}

/* newsletter */
.newsletter{top:3139px;height:279px;background:var(--white);text-align:center}
.newsletter .section-title{margin-top:42px;font-size:30px}
.newsletter p{font-weight:600;color:var(--ink);font-size:16px;margin-top:26px}
.signup{display:flex;width:566px;margin:24px auto 0;height:42px;border:1px solid #ccc;border-radius:21px;overflow:hidden}
.signup span{flex:1;text-align:left;padding:12px 24px;font-size:14px;color:var(--muted)}
.signup b{width:126px;background:var(--blue);color:var(--white);font-size:15px;padding-top:12px;letter-spacing:.5px}

/* contact bar */
.contact-bar{top:3418px;height:86px;background:var(--blue);color:var(--white)}
.contact-bar h2{position:absolute;left:164px;top:22px;font-family:"Oswald",sans-serif;font-size:30px;font-weight:500}
.contact-item{position:absolute;top:16px;display:flex;align-items:center;gap:18px;font-size:17px;line-height:1.25}

/* footer */
.site-footer{top:3504px;height:146px;background:var(--navy);color:var(--white)}
.foot-nav{position:absolute;left:136px;top:26px;display:flex;gap:30px;font-family:"Oswald",sans-serif;font-size:13px}
.foot-social{position:absolute;left:136px;top:58px;display:flex;gap:16px}
.foot-social i{width:18px;height:18px;border-radius:50%;background:var(--white);display:block}
.copy{position:absolute;left:136px;top:98px;font-size:13px}
.partner{position:absolute;right:118px;top:50px;display:flex;align-items:center;gap:10px}
.partner-mark{width:34px;height:34px;background:#5d7fa6}
.partner-name{font-family:"Hind",sans-serif;font-size:22px;font-weight:500;color:#8ea9c9;line-height:1;letter-spacing:1px}

/* legal */
.legal{top:3650px;height:132px;background:var(--white)}
.legal p{position:absolute;left:130px;top:34px;width:940px;text-align:center;font-size:12.5px;line-height:2.6;color:var(--text)}
.legal .code{position:absolute;right:30px;top:84px;font-weight:600;font-size:13px;color:var(--ink)}
</style>
</head>
<body>

<header class="site-header">
  <div class="brand">
    <div class="brand-mark"></div>
    <div>
      <div class="brand-name">THE HALVICK CREW</div>
      <div class="brand-sub">HOME LOAN GROUP</div>
    </div>
  </div>
  <div class="head-contact" style="left:536px">
    <div class="icon-circle"><svg width="22" height="28" viewBox="0 0 22 28"><path d="M11 0C5 0 0 5 0 11c0 8 11 17 11 17s11-9 11-17C22 5 17 0 11 0z" fill="#fff"/><circle cx="11" cy="11" r="4" fill="#1a6fb9"/></svg></div>
    <div>4120 Larkspur Ave, Suite 310,<br>Maple City FL 30410</div>
  </div>
  <div class="head-contact" style="left:870px">
    <div class="icon-circle"><svg width="26" height="26" viewBox="0 0 24 24"><path d="M6.6 10.8a15.1 15.1 0 0 0 6.6 6.6l2.2-2.2c.3-.3.7-.4 1-.2 1.1.4 2.300.6 3.6.6.6 0 1 .4 1 1V20c0 .6-.4 1-1 1A17 17 0 0 1 3 4c0-.6.4-1 1-1h3.5c.6 0 1 .4 1 1 0 1.3.2 2.5.6 3.6.1.3 0 .7-.2 1z" fill="#fff"/></svg></div>
    <div>Call Us<div class="phone-big">1-555-014-7202</div></div>
  </div>
  <nav class="main-nav"><span class="active">HOME</span><span>ABOUT</span><span>MORTGAGE 101</span><span>CONTACT</span></nav>
</header>

<section class="hero" role="img" aria-label="Hands setting a small wooden house model on blocks labelled mortgage, soft blue bokeh background">
  <div class="hero-photo"></div>
  <div class="hero-copy">
    <h1>HALVICK CREW</h1>
    <p>Vitae risus nulla aenean ut accumsan. Nostra lectus purus inceptos vestibulum pellentesque neque nulla sollicitudin pede neque sapien.</p>
    <span class="btn">CALL US TODAY</span>
  </div>
  <div class="hero-arrows">
    <svg width="22" height="40" viewBox="0 0 22 40"><path d="M20 2 3 20l17 18" stroke="#fff" stroke-width="3" fill="none"/></svg>
    <svg width="22" height="40" viewBox="0 0 22 40"><path d="M2 2l17 18L2 38" stroke="#fff" stroke-width="3" fill="none"/></svg>
  </div>
</section>

<section class="intro">
  <div class="intro-head">
    <h2 class="section-title">The Halvick Crew <span>Home Loan Group</span></h2>
    <div class="rule"></div>
  </div>
  <p class="lead">Aliquam molestie, mi et imperdiet euismod, dui purus auctor tellus, et interdum lacus lectus et ante. Sed accumsan sollicitudin sapien, sit amet adipiscing turpis gravida ac. In congue, neque ac lobortis volutpat, libero mauris varius mi, vitae suscipit ipsum ligula vitae risus. Duis aliquam nibh a dui iaculis viverra id a velit. Vivamus egestas risus in magna varius commodo.</p>
  <div class="intro-btn"><span class="btn">READ MORE</span></div>
  <div class="cards" style="top:267px">
    <div class="card">
      <div class="card-media" role="img" aria-label="Video: a couple meeting with their loan officer at a table" style="background:linear-gradient(135deg,#cfc9c0,#8d8479)"><span class="play"></span></div>
      <p class="card-text">Placerat vehicula id suspendisse lorem eget. Vel et gravida. Non a dapibus eget scelerisque quisque curabitur leo wisi pulvinar erat morbi.</p>
    </div>
    <div class="card">
      <div class="card-media" role="img" aria-label="Video: a grey two-storey family home under a blue sky" style="background:linear-gradient(180deg,#8fb4d8,#9aa3a8 55%,#6f7d5a)"><span class="play"></span></div>
      <p class="card-text">Placerat vehicula id suspendisse lorem eget. Vel et gravida. Non a dapibus eget scelerisque quisque curabitur leo wisi pulvinar erat morbi.</p>
    </div>
    <div class="card">
      <div class="card-media" role="img" aria-label="Video: a modern white house with a pool and palm trees" style="background:linear-gradient(180deg,#6aa3d8,#d7dde0 55%,#3f9bc4)"><span class="play"></span></div>
      <p class="card-text">Placerat vehicula id suspendisse lorem eget. Vel et gravida. Non a dapibus eget scelerisque quisque curabitur leo wisi pulvinar erat morbi.</p>
    </div>
  </div>
</section>

<section class="blog">
  <h2 class="section-title">Our <span>Blog</span></h2>
  <div class="rule"></div>
  <div class="cards" style="top:124px">
    <div class="card">
      <div class="card-media" role="img" aria-label="A family standing outside their new home" style="background:linear-gradient(135deg,#9c8a7a,#5f5248)"><div class="date-badge"><b>01</b><small>FEB</small></div></div>
      <p class="card-text">Placerat vehicula id suspendisse lorem eget. Vel et gravida. Non a dapibus eget scelerisque quisque curabitur leo wisi pulvinar erat morbi.</p>
      <div class="center" style="margin-top:16px"><span class="btn">READ MORE</span></div>
    </div>
    <div class="card">
      <div class="card-media" role="img" aria-label="A couple sitting on the front steps of a yellow house" style="background:linear-gradient(135deg,#c9b15a,#6b7a6a)"><div class="date-badge"><b>01</b><small>FEB</small></div></div>
      <p class="card-text">Placerat vehicula id suspendisse lorem eget. Vel et gravida. Non a dapibus eget scelerisque quisque curabitur leo wisi pulvinar erat morbi.</p>
      <div class="center" style="margin-top:16px"><span class="btn">READ MORE</span></div>
    </div>
    <div class="card">
      <div class="card-media" role="img" aria-label="A smiling family group outdoors" style="background:linear-gradient(135deg,#a98f78,#5a4a40)"><div class="date-badge"><b>01</b><small>FEB</small></div></div>
      <p class="card-text">Placerat vehicula id suspendisse lorem eget. Vel et gravida. Non a dapibus eget scelerisque quisque curabitur leo wisi pulvinar erat morbi.</p>
      <div class="center" style="margin-top:16px"><span class="btn">READ MORE</span></div>
    </div>
  </div>
</section>

<section class="team">
  <h2 class="section-title">Our <span>Team</span></h2>
  <div class="rule"></div>
  <div class="lead-photo" role="img" aria-label="Portrait of Elias Halvick"></div>
  <div class="lead-info">
    <h3>ELIAS HALVICK</h3>
    <div class="role">Producing Branch Manager</div>
    Bramfield Home Loans, Inc – NMLS 40117<br>
    Elias.Halvick@bramfieldloans.example<br>
    Office: (555) 010-5050<br>
    Fax: (555) 010-8232
  </div>
  <p class="bio">I have over 15 years of experience in Mortgage Planning. I rank in the top 1% of loan originators in the country. I pride myself on making the home buying process as smooth as possible. I will guide you through the mortgage process and look forward to helping you with your transaction. My team has been awarded with the Circle of Excellence award and CEO Club for being in the top 5 teams in the country having helped over 700+ families achieve the dream of home ownership between the years 2016 and 2017 and counting.</p>

  <div class="member" style="left:82px">
    <div class="avatar" role="img" aria-label="Portrait of Marco Tellez"></div>
    <h4>MARCO TELLEZ</h4>
    Loan Partner I - NMLS ID 2093318<br>MarcoTellez@bramfieldloans.example<br>(555) 014-7202
    <div class="socials"><i></i><i></i><i></i></div>
  </div>
  <div class="member" style="left:437px">
    <div class="avatar" role="img" aria-label="Portrait of Rafael Ostin"></div>
    <h4>RAFAEL OSTIN</h4>
    Loan Processor - NMLS ID: 2087614<br>Rafael.Ostin@bramfieldloans.example<br>(555) 010-9294
    <div class="socials"><i></i><i></i><i></i></div>
  </div>
  <div class="member" style="left:800px">
    <div class="avatar" role="img" aria-label="Portrait of Dana Marrow" style="background:radial-gradient(circle at 50% 42%,#d9b08a,#b58a4a 55%,#1c1c1c 56%)"></div>
    <h4>DANA MARROW</h4>
    Closing Coordinator/Team Leader–NMLS 2075530<br>Dana.Marrow@bramfieldloans.example<br>(555) 010-1151
    <div class="socials"><i></i><i></i><i></i></div>
  </div>
</section>

<section class="resources" role="img" aria-label="Faded backdrop of a waterfront home with palm trees">
  <div class="resources-veil"></div>
  <div class="resources-inner">
    <h2 class="section-title">Resources</h2>
    <div class="rule"></div>
    <p>Nec wisi tincidunt vehicula ipsum vel magna sit amet. Eleifend orci ac. Lectus vivamus risus metus vero integer imperdiet aenean dolor. Auctor ipsum libero. Mi suspendisse hac. Id sapien accumsan. Nascetur sit neque viverra mi justo ut lorem so- ciosqu erat a a. Varius perferendis suspendisse. Placerat vehicula id suspendisse lorem eget. Vel et gravida. Non a dapibus eget scelerisque quisque curabitur leo wisi pulvinar erat morbi. Sociosqu enim nisl et volutpat sem.</p>
    <span class="btn">DOWNLOAD</span>
  </div>
</section>

<section class="newsletter">
  <h2 class="section-title">Join E-mail Newsletter</h2>
  <div class="rule"></div>
  <p>Aliquam molestie, mi et imperdiet euismod, dui purus auctor tellus, et interdum lacus lectus et ante.</p>
  <div class="signup"><span>Your Email Address</span><b>SIGN UP</b></div>
</section>

<section class="contact-bar">
  <h2>CONTACT US</h2>
  <div class="contact-item" style="left:456px">
    <svg width="24" height="32" viewBox="0 0 22 28"><path d="M11 0C5 0 0 5 0 11c0 8 11 17 11 17s11-9 11-17C22 5 17 0 11 0z" fill="#fff"/><circle cx="11" cy="11" r="4" fill="#1a6fb9"/></svg>
    <div>4120 Larkspur Ave, Suite 310,<br>Maple City FL 30410</div>
  </div>
  <div class="contact-item" style="left:792px">
    <svg width="30" height="30" viewBox="0 0 24 24"><path d="M6.6 10.8a15.1 15.1 0 0 0 6.6 6.6l2.2-2.2c.3-.3.7-.4 1-.2 1.1.4 2.3.6 3.6.6.6 0 1 .4 1 1V20c0 .6-.4 1-1 1A17 17 0 0 1 3 4c0-.6.4-1 1-1h3.5c.6 0 1 .4 1 1 0 1.3.2 2.5.6 3.6.1.3 0 .7-.2 1z" fill="#fff"/></svg>
    <div>Call Us<div class="phone-big" style="color:#fff">1-555-014-7202</div></div>
  </div>
</section>

<footer class="site-footer">
  <nav class="foot-nav"><span>HOME</span><span>ABOUT</span><span>MORTGAGE 101</span><span>CONTACT US</span></nav>
  <div class="foot-social"><i></i><i></i><i></i><i></i><i></i></div>
  <div class="copy">Copyright © 2018. Company Name .All Right Reserved &nbsp; | &nbsp; Privacy Policy &nbsp; | &nbsp; Terms</div>
  <div class="partner">
    <div class="partner-mark"></div>
    <div class="partner-name">BRAMFIELD<br>HOME LOANS</div>
  </div>
</footer>

<section class="legal">
  <p>Licensed by the Office of Trade Stewardship under the Regional Credit Providers Act. Loans made or arranged pursuant to a Regional Credit Providers Act License. Equal Housing Lender Bramfield Cannot Accept mortgage applications for properties located in New York via this site.</p>
  <span class="code">M1</span>
</section>

</body>
</html>
```